My wife is a classical pianist and she is organising a tango event. This will consist of her playing piano, a singer, a saxophonist and 2 tango dancers. I want the flyer to capture the colour, vibrancy of tango. Details to be included on the flyer are below.

I need the final design to be in psd so can change words and move things about if necessary and also change the flyer for future events. I don't want you to use the image attached but this gives an idea of tango. I need the flyer in portrait.

The Heart of Milonga
A night of Tango music and dance.

Date: 16th of November [url removed, login to view] pm

Venue: Carrow Hall. 17 Fenwick Row London, N4 2QB
Nearest Tubes: Holbeck Lane Station. Eastgate Line

Performers: Lina Voretti ( soprano)
Gianluca Bertolazzi- Morales ( sax)
Corinne Valdemar ( piano)

Dancers: Renato da Silveira
Noemie

Music by Ettore Balzani, Iván Malvedo, Tomas Quiroga, Julio Benvar, Fermin Lozada, Corinne Valdemar.

Tickets: £15 conc. £10
Tickets on the door or online
For more information
[url removed, login to view]
01632960418

```html
<!DOCTYPE html>
<html lang="en">
<head>
<meta charset="utf-8">
<title>The Heart of Milonga</title>
<link rel="stylesheet" href="https://fonts.googleapis.com/css2?family=Pinyon+Script&family=Crimson+Text&family=Tinos:ital,wght@1,400&display=swap">
<style>
  :root {
    --night: #000000;
    --wine: #6e0a2c;
    --wine-deep: #2a0312;
    --gold: #f0d566;
    --gold-dark: #b8922a;
    --cream: #f5e39a;
    --detail: #f2d04a;
    --figure-light: rgba(220, 220, 220, 0.75);
    --figure-mid: rgba(120, 120, 120, 0.5);
  }
  * { margin: 0; padding: 0; box-sizing: border-box; }
  html, body {
    width: 960px;
    height: 1200px;
    overflow: hidden;
    background: var(--night);
  }
  .flyer {
    position: relative;
    width: 960px;
    height: 1200px;
    overflow: hidden;
    background:
      radial-gradient(ellipse 360px 520px at 600px 640px, var(--wine) 0%, var(--wine-deep) 55%, var(--night) 100%);
  }
  .dancers-art {
    position: absolute;
    left: 250px;
    top: 200px;
    width: 620px;
    height: 1000px;
    background:
      radial-gradient(ellipse 150px 300px at 320px 280px, var(--figure-light) 0%, var(--figure-mid) 55%, transparent 100%),
      radial-gradient(ellipse 260px 380px at 280px 680px, var(--figure-mid) 0%, rgba(60,60,60,0.3) 60%, transparent 100%);
  }
  .title {
    position: absolute;
    top: 40px;
    left: 0;
    width: 960px;
    text-align: center;
    font-family: "Pinyon Script", cursive;
    font-size: 104px;
    line-height: 1.2;
    color: var(--gold);
    background: linear-gradient(180deg, #fff2a8 0%, var(--gold) 45%, var(--gold-dark) 100%);
    -webkit-background-clip: text;
    background-clip: text;
    -webkit-text-fill-color: transparent;
  }
  .tagline {
    position: absolute;
    top: 234px;
    left: 0;
    width: 1000px;
    text-align: center;
    font-family: "Crimson Text", serif;
    font-size: 33px;
    color: var(--cream);
    letter-spacing: 0.5px;
  }
  .details {
    position: absolute;
    left: 28px;
    font-family: "Tinos", serif;
    font-style: italic;
    font-size: 26px;
    line-height: 29px;
    color: var(--detail);
  }
  .details p { white-space: nowrap; }
  .event-info { top: 450px; }
  .performers { top: 580px; }
  .dancers { top: 734px; }
  .composers { top: 854px; }
  .tickets { top: 1036px; }
</style>
</head>
<body>
  <main class="flyer">
    <div class="dancers-art" role="img" aria-label="Silhouette of a tango couple dancing, lit from above"></div>

    <h1 class="title">The Heart of Milonga</h1>
    <p class="tagline">A night of Tango music and dance</p>

    <section class="details event-info">
      <p>Date: 16th of November 7.30 pm</p>
      <p>Venue: Carrow Hall. 17 Fenwick Row London, N4 2QB</p>
      <p>Nearest Tubes: Holbeck Lane Station. Eastgate Line</p>
    </section>

    <section class="details performers">
      <p>Performers:</p>
      <p>Lina Voretti ( soprano)</p>
      <p>Gianluca Bertolazzi- Morales ( sax)</p>
      <p>Corinne Valdemar ( piano)</p>
    </section>

    <section class="details dancers">
      <p>Dancers:</p>
      <p>Renato da Silveira</p>
      <p>Noemie</p>
    </section>

    <section class="details composers">
      <p>Music by</p>
      <p>Ettore Balzani, Iván Malvedo, Tomas Quiroga,</p>
      <p>Julio Benvar, Fermin Lozada, Corinne Valdemar.</p>
    </section>

    <section class="details tickets">
      <p>Tickets: £15 conc. £10</p>
      <p>Tickets on the door or online</p>
      <p>For more information</p>
      <p>www.corinnevaldemar.com</p>
      <p>01632960418</p>
    </section>
  </main>
</body>
</html>
```